Business card design needed

I need a business card for a new company based in Perth, Western Australia, called KT Power Pty Ltd.

I'm the sole proprietor, and have 25 years' experience in directorship, senior commercial/business development/strategy roles in the oil & gas industry with both supermajors and junior listed companies. I also have interests in renewable energy (and am co-founder and director of a separate renewable energy start-up company). KT Power will be the vehicle for me to contract my services, principally in the oil & gas industry (although this will include directorship services to the renewable energy company). These services will include general consultancy in my areas of expertise, and contracting to provide senior management/director services to start-up or junior oil and gas companies.

I'm looking for a design that communicates professionalism, dynamism, experience, strategic skills and growth.

My ConnectHub profile may also be useful context;

"I have a real passion for discovering new investment opportunities and turning them from talk into reality. Right now my focus is on oil, gas and energy ventures. I’m always on the look out for compelling new investment opportunities where I can bring my leadership and strategic insight to bear to make a real difference by delivering transformational results.

I spent 24 years with HX where I built up extensive international experience in oil, gas and energy and was a member of the company’s “fast track” development programme. As an entrepreneurial senior commercial leader, strategic thinker and tactical dealmaker I was responsible for numerous deals such as divestments, farm-ins, asset swaps, new acreage bids, unitizations, gas and LNG sales, creating billions of dollars of value for HX. These deals frequently broke new ground and/or required an innovative approach that delivered results in excess of what the business thought achievable. I have held senior executive and director roles covering Exploration & Production, Mergers & Acquisitions, Business Development, LNG Marketing, Joint Venture Management, Gas & Power and Corporate head office. International assignments included UK, Australia, Indonesia, Norway & Belgium.

I’m a member of the Guild of Global Fuel Brokers (GGFB) and the Southern Council of Board Members (SCBM).

Board experience comprises four directorships and two alternate directorships of Australian companies, and directorship of a Not for Profit organisation.

Specialties
Strategy, Business Development, Mergers & Acquisitions, Joint Venture Management, Negotiation, Gas & LNG Marketing."

Target Market(s)

Oil and gas or energy companies of all sizes from large listed companies to start-ups - also service providers to the industry.

Industry/Entity Type

Oil And Gas

Contact Information for Business Card

KT Power Pty Ltd
Daniel Hobart
27C Lorne Avenue,
Kelmsdale,
WA 6093

Tel +61 455 823 617
email hobartdk@vellimo.net.au

```html
<!DOCTYPE html>
<html lang="en">
<head>
<meta charset="utf-8">
<title>KT Power Pty Ltd — Business Card</title>
<link rel="stylesheet" href="https://fonts.googleapis.com/css2?family=Exo+2:wght@600;700&family=Roboto+Condensed:wght@300;400;700&display=swap">
<style>
  :root {
    --backdrop: #d9d9d9;
    --card-black: #161616;
    --card-white: #ffffff;
    --brand-red: #d0202e;
    --brand-grey: #5b5b5b;
    --ink: #3a3a3a;
  }
  * { margin: 0; padding: 0; box-sizing: border-box; }
  html, body {
    width: 1200px; height: 900px; overflow: hidden;
    background: var(--backdrop);
  }
  .sheet {
    width: 1200px; height: 900px;
    display: flex; flex-direction: column; align-items: center; justify-content: center;
    gap: 56px;
  }
  .card {
    position: relative;
    width: 630px; height: 360px;
    box-shadow: 0 6px 18px rgba(0,0,0,0.18);
    overflow: hidden;
  }

  /* Brand name */
  .brand { display: flex; align-items: center; gap: 14px; }
  .brand-square { width: 34px; height: 34px; background: var(--brand-red); flex: none; }
  .brand-name {
    font-family: "Exo 2", sans-serif; font-weight: 700;
    text-transform: uppercase; letter-spacing: 1px; line-height: 1;
  }

  /* Back */
  .card-back { background: var(--card-black); }
  .card-back .brand { position: absolute; left: 110px; top: 110px; }
  .card-back .brand-square { width: 56px; height: 56px; }
  .card-back .brand-name { font-size: 50px; color: var(--brand-grey); }
  .services {
    position: absolute; left: 110px; right: 40px; top: 232px;
    font-family: "Roboto Condensed", sans-serif; font-weight: 300;
    font-size: 14px; letter-spacing: 0.6px; line-height: 1.45;
    color: var(--brand-red); text-transform: uppercase;
  }

  /* Front */
  .card-front { background: var(--card-white); }
  .card-front .brand { position: absolute; left: 120px; top: 84px; }
  .card-front .brand-name { font-size: 40px; color: var(--ink); }
  .edge-stripe {
    position: absolute; left: 0; top: 0; bottom: 0; width: 10px;
    background: var(--brand-red);
  }
  .name-tag {
    position: absolute; left: 0; top: 196px;
    background: var(--brand-red); color: #fff;
    padding: 9px 22px 9px 120px;
    font-family: "Roboto Condensed", sans-serif; font-weight: 700;
    font-size: 19px; letter-spacing: 1px; text-transform: uppercase;
  }
  .contact {
    position: absolute; left: 120px; top: 248px;
    font-family: "Roboto Condensed", sans-serif; font-weight: 300;
    font-size: 15px; line-height: 1.4; color: var(--ink);
    text-transform: uppercase; letter-spacing: 0.4px;
  }
  .contact .address { margin-bottom: 8px; }
  .contact .label { color: var(--brand-red); font-weight: 400; }
</style>
</head>
<body>
<main class="sheet">
  <section class="card card-back" aria-label="Card back">
    <div class="brand">
      <span class="brand-square"></span>
      <span class="brand-name">KT Power Pty Ltd</span>
    </div>
    <p class="services">
      Strategy | Business Development | Mergers &amp; Acquisitions<br>
      Joint Venture Management | Negotiation | Gas | LNG Marketing
    </p>
  </section>

  <section class="card card-front" aria-label="Card front">
    <span class="edge-stripe"></span>
    <div class="brand">
      <span class="brand-square"></span>
      <span class="brand-name">KT Power Pty Ltd</span>
    </div>
    <div class="name-tag">Daniel Hobart</div>
    <div class="contact">
      <p class="address">27C Lorne Avenue, Kelmsdale,<br>WA 6093</p>
      <p><span class="label">P:</span> +61 455 823 617</p>
      <p><span class="label">E:</span> hobartdk@vellimo.net.au</p>
    </div>
  </section>
</main>
</body>
</html>
```